Business Card Design Project

HI! Can you design a business card with the logo you designed for me? I don't know what the typical order is so can you place it in the order most people do? White background and also play with a couple of colored backgrounds. Thank you!

Darnette Ruval-Koskin
darnette@sunmorrowcoaching.com
sunmorrowcoaching.com
555-317-4082

Target Market(s)

Women

Industry/Entity Type

Business

```html
<!DOCTYPE html>
<html lang="en">
<head>
<meta charset="utf-8">
<title>Sunmorrow Coaching Services – Business Card</title>
<link rel="stylesheet" href="https://fonts.googleapis.com/css2?family=Roboto+Condensed:wght@300;400&display=swap">
<style>
  :root {
    --stage: #3d3d3d;
    --card-white: #ffffff;
    --brand-orange: #f7961f;
    --brand-red: #c1202f;
    --tagline-grey: #4d4d4f;
    --text-white: #ffffff;
  }
  html, body {
    margin: 0;
    width: 1200px;
    height: 900px;
    overflow: hidden;
    background: var(--stage);
  }
  .canvas {
    position: relative;
    width: 1200px;
    height: 900px;
  }
  .business-card {
    position: absolute;
    left: 188px;
    top: 206px;
    width: 832px;
    height: 490px;
    font-family: "Roboto Condensed", "Arial Narrow", sans-serif;
  }
  .card-base { fill: var(--card-white); }
  .accent-panel { fill: var(--brand-orange); }
  .contact-band { fill: var(--brand-red); }
  .brand-dot { fill: var(--brand-orange); }
  .brand-name {
    fill: var(--brand-red);
    font-weight: 400;
    font-size: 66px;
  }
  .brand-tagline {
    fill: var(--tagline-grey);
    font-weight: 400;
    font-size: 24px;
    letter-spacing: 4px;
  }
  .phone-line {
    fill: var(--text-white);
    font-weight: 300;
    font-size: 24px;
  }
  .person-name {
    fill: var(--text-white);
    font-weight: 300;
    font-size: 36px;
  }
  .name-rule { stroke: var(--text-white); stroke-width: 2; }
  .contact-detail {
    fill: var(--text-white);
    font-weight: 300;
    font-size: 21px;
  }
</style>
</head>
<body>
<main class="canvas">
  <svg class="business-card" viewBox="0 0 832 490" xmlns="http://www.w3.org/2000/svg" aria-label="Sunmorrow Coaching Services business card">
    <defs>
      <clipPath id="card-shape">
        <rect width="832" height="490" rx="14" ry="14"/>
      </clipPath>
    </defs>
    <g clip-path="url(#card-shape)">
      <rect class="card-base" width="832" height="490"/>
      <polygon class="accent-panel" points="370,0 832,0 832,490 493,490"/>
      <polygon class="contact-band" points="0,422 475,422 486,461 0,461"/>
    </g>

    <g class="brand-block">
      <circle class="brand-dot" cx="241" cy="175" r="60"/>
      <text class="brand-name" x="241" y="314" text-anchor="middle">Sunmorrow</text>
      <text class="brand-tagline" x="72" y="354" textLength="337" lengthAdjust="spacing">COACHING SERVICES</text>
    </g>

    <text class="phone-line" x="234" y="449" text-anchor="middle">Touch With Us: 555-317-4082</text>

    <g class="contact-block">
      <text class="person-name" x="494" y="286" textLength="290" lengthAdjust="spacingAndGlyphs">Darnette Ruval-Koskin</text>
      <line class="name-rule" x1="492" y1="299" x2="786" y2="299"/>
      <text class="contact-detail" x="494" y="325">darnette@sunmorrowcoaching.com</text>
      <text class="contact-detail" x="494" y="351">sunmorrowcoaching.com</text>
    </g>
  </svg>
</main>
</body>
</html>
```